Bottle labels and logo for small distillery

Harbor Stillhouse is a small beginning project of handcrafted distillery producing cider spirit (same as apple wine spirit) and apple vodka from apple wine. There are not many similar small distilleries in the Baltic Sea region and very few of them produce apple brandy, so the concept and the product itself are unique. That is the reason we are not developing any distinctive brand and we are sticking to two elements – company name ‘Harbor Stillhouse OÜ’ and product name ‘Orchardine’. Best branding solution for us would be to have a clear logo instead of words.

In the future it is most likely that the product range will broaden by some type of sweet liqueurs like apple-liqueur and black-currant-liqueur and both will be mixtures of natural juice and apple brandy.

We have tested the product itself and more or less chosen proper bottle and closing. Example of the shape of the bottle:

https://www.vessel-depot.example.co.uk/Glass-vessels/Glass-vessels/500ml-glass-vessels/500ml-clear-glass-vessel-Rondel.html

Sizes of bottles:
500 ml Height (without cap) 350 mm, external diameter 60 mm;
375 ml Height (without cap) 330 mm, external diameeter 55 mm;

The bottle cap/closing is going to be waxed, and should look something like that:

http://img.picstash-example.com/qR7Tz.jpg

The design has two separate parts: (1) paper bottle label and (2) print on the bottle.

Front side – printed to the bottle, preferably a symbol without text, for better quality of print rather a vector graphics (monochrome or up to 3-single colour picture). We would like to use the symbol also as an enterprise logo if possible (but logo and bottle print can also be different if designer decides so). It should give a hint to apple based distillate (but, we do not want to narrow down creators fantasy so if you have a good idea please don’t hold back). Just to offer a dumb examples:
https://moodbinder-example.com/entry/51839206
https://www.pinboardly-example.ca/pin/719302846615902418/?lp=true https://www.stockframe-example.com/image-vector/decorative-apple-flora-ornaments-leaf-flower-482017356?src=QXP_tbRkLw8YpH3JcV_29m-2-50
NB! these are just examples of style, contents are more or less random.

Back side – a rectangular shaped label glued to the bottle. Label should not be a square but rather oblong and narrow. The colour of the label shouldn’t be white but rather light yellow, light brown or light creamy. Some examples:

https://www.pinboardly-example.co.uk/pin/830174529266108354 https://www.pinboardly-example.co.uk/pin/591840372605183924

Label has to contain such information:
1) (Product in large print) Orchardine
2) (product) apple wine spirit
3) (Neto amount) 50 cl; / 35 cl
4) (Ethanol in large print) 45%; / 55%
5) (Producer) Produced by Harbor Stillhouse, Lõunamaa 48213, Rannaküla, Sõstra 7;
6) (raw material and technology) Made in Estonia. Product is made of Estonian apple wine and distilled in reflux still in small batches
7) (distillate) Distillate 85%
8) (batch no) Batch no: (stamp) …
9) (note) produced with utmost pleasure
10) (note) Consume responsibly
11) (signature) distiller: …

We also need the label to be designed in Estonian as follows:
1) Orchardine
2) Õunaveini destillaat
3) 50 cl; / 35 cl
4) 45% / 55%
5) Toodetud Harbor Stillhouse OÜ poolt, Lõunamaal 48213, Rannaküla, Sõstra 7;
6) Toodetud Eestis, eestimaisest õunaveinist ja destilleeritud käsitööna väikeste partiidena
7) Destillaat 85%
8) Partii nr:
9) Toodetud puhtast rõõmust
10) Tarbige vastutustundlikult!
11) Meister:

Design as such can be the same. Since we are planning to bottle the product in 375 ml and 500 ml bottles and dilute it down to 45% and 55%. So, there should be 37,5 cl 45%, 50 cl 45%; 37,5 cl 55%; 50 cl 55%.

We assume that in case of 37,5 cl and 50 cl bottles we can use the same design and just resize the printed image and paper-label a bit.

Since the product is handmade and high quality we would like to stress credibility. Not as important as the first purchase is the second purchase of clients – the label should not be shocking but rather trustworthy. And classy in the very best sense.

We are hoping to have a long term business relationship with possible future designer.

Target Market(s)

Adult male alcohol consumers

Industry/Entity Type

Food Production

Logo Text

Harbor Stillhouse

Colors

Designer to choose colors to be used in the design.

```html
<!DOCTYPE html>
<html lang="en">
<head>
<meta charset="utf-8">
<title>Orchardine – bottle print and back label</title>
<link rel="stylesheet" href="https://fonts.googleapis.com/css2?family=Old+Standard+TT:ital,wght@0,400;0,700;1,400&family=Dancing+Script:wght@400&display=swap">
<style>
  :root {
    --backdrop: #ffffff;
    --ink: #1f1f1f;
    --label-paper: #f3eee1;
    --label-edge: #d9d1bd;
    --accent-red: #9c2f37;
    --accent-navy: #2d3d6b;
    --rule: #6b6558;
    --print-dark: #141414;
    --print-mid: #3a3a3a;
  }
  * { box-sizing: border-box; margin: 0; padding: 0; }
  html, body {
    width: 924px; height: 1200px; overflow: hidden;
    background: var(--backdrop);
  }
  .canvas {
    position: relative; width: 924px; height: 1200px;
    font-family: "Old Standard TT", Georgia, serif; color: var(--ink);
  }

  /* Front: printed symbol area */
  .bottle-print {
    position: absolute; left: 70px; top: 420px;
    width: 340px; height: 340px;
    border-radius: 50% 50% 8px 8px;
    background: radial-gradient(circle at 50% 40%, var(--print-mid), var(--print-dark) 70%);
  }

  /* Back: paper label */
  .back-label {
    position: absolute; left: 480px; top: 300px;
    width: 380px; height: 600px;
    background: var(--label-paper);
    border: 1px solid var(--label-edge);
    padding: 34px 30px 26px;
    display: flex; flex-direction: column; align-items: center;
    text-align: center;
  }
  .product-name {
    font-size: 46px; font-weight: 400; letter-spacing: 2px; line-height: 1;
  }
  .product-type {
    margin-top: 6px; font-size: 17px; font-style: italic; color: var(--accent-red);
  }
  .facts {
    margin-top: 22px; width: 100%;
    display: flex; justify-content: space-between; align-items: stretch;
  }
  .fact-box {
    border: 1px solid var(--rule); padding: 8px 12px;
    font-size: 16px; line-height: 1.2;
  }
  .fact-box .fact-label { display: block; font-size: 13px; }
  .fact-box--net { width: 110px; }
  .fact-box--ethanol { width: 120px; font-size: 20px; }
  .fact-box--ethanol .fact-label { font-size: 18px; }
  .producer {
    margin-top: 22px; font-size: 15px; line-height: 1.35;
  }
  .origin {
    margin-top: 16px; width: 100%;
    border: 1px solid var(--rule); padding: 8px 10px;
    font-size: 14px; line-height: 1.35;
  }
  .distillate { margin-top: 14px; font-size: 15px; line-height: 1.3; }
  .note-pleasure {
    margin-top: 16px; font-size: 17px; font-style: italic; color: var(--accent-navy);
  }
  .note-pleasure::after {
    content: ""; display: block; width: 100%; height: 1px;
    background: var(--accent-red); margin-top: 3px;
  }
  .note-responsible {
    margin-top: 14px; font-size: 15px; color: var(--accent-red);
  }
  .label-footer {
    margin-top: auto; width: 100%;
    display: flex; justify-content: space-between; align-items: flex-end;
  }
  .distiller-sign {
    font-family: "Dancing Script", cursive; font-size: 24px;
  }
  .batch-stamp {
    width: 130px; height: 56px;
    border: 1.5px dashed var(--rule);
    font-size: 12px; padding: 4px 6px; text-align: center;
  }
</style>
</head>
<body>
<main class="canvas">
  <div class="bottle-print" role="img" aria-label="Black silhouette of an apple tree bearing apples, printed on the bottle front"></div>

  <section class="back-label">
    <h1 class="product-name">ORCHARDINE</h1>
    <p class="product-type">apple wine spirit</p>

    <div class="facts">
      <div class="fact-box fact-box--net"><span class="fact-label">Net amount</span>50 cl</div>
      <div class="fact-box fact-box--ethanol"><span class="fact-label">Ethanol</span>45%</div>
    </div>

    <p class="producer">Produced by<br>Harbor Stillhouse, Lõunamaa 48213,<br>Rannaküla, Sõstra 7</p>

    <p class="origin">Made in Estonia<br>Product is made of Estonian apple wine and distilled in reflux still in small batches</p>

    <p class="distillate">Distillate<br>85%</p>

    <p class="note-pleasure">produced with utmost pleasure</p>
    <p class="note-responsible">Consume responsibly</p>

    <div class="label-footer">
      <span class="distiller-sign">distiller</span>
      <div class="batch-stamp">batch no</div>
    </div>
  </section>
</main>
</body>
</html>
```